" Empresa jurídica moderna e atuante com foco no segmento empresarial, conta com diferencial de propor uma maior aproximaçao com as empresas/clientes, solucionando seus problemas e prevendo suas necessidades. "

```html
<!DOCTYPE html>
<html lang="pt-BR">
<head>
<meta charset="UTF-8">
<title>Moreira, Campos &amp; Lacerda — Pasta</title>
<link rel="stylesheet" href="https://fonts.googleapis.com/css2?family=Cinzel:wght@400&family=Montserrat:wght@400;600&display=swap">
<style>
  :root {
    --navy: #2d4a7b;
    --navy-dark: #24406d;
    --paper: #ffffff;
    --paper-shade: #f1f2f5;
    --ink: #3b4f78;
    --rule: #c9cfdc;
    --backdrop: #e7e8ea;
  }
  html, body {
    margin: 0;
    padding: 0;
    width: 1200px;
    height: 1200px;
    overflow: hidden;
    background: var(--backdrop);
  }
  .canvas {
    position: relative;
    width: 1200px;
    height: 1200px;
  }
  .folder-flap {
    position: absolute;
    left: 0;
    top: 0;
  }
  .folder-cover {
    position: absolute;
    left: 175px;
    top: 206px;
    width: 475px;
    height: 730px;
    background: var(--navy);
  }
  .folder-inside {
    position: absolute;
    left: 650px;
    top: 206px;
    width: 480px;
    height: 730px;
    background: linear-gradient(180deg, var(--paper) 0%, var(--paper) 70%, var(--paper-shade) 100%);
  }
  .brand {
    position: absolute;
    text-align: center;
    color: var(--paper);
  }
  .brand-name {
    font-family: "Cinzel", serif;
    font-weight: 400;
    white-space: nowrap;
    letter-spacing: 0.5px;
  }
  .brand-tagline {
    font-family: "Montserrat", sans-serif;
    font-weight: 400;
    text-transform: uppercase;
    white-space: nowrap;
  }
  .brand--cover {
    left: 0;
    width: 475px;
    top: 78px;
  }
  .brand--cover .brand-name { font-size: 17px; }
  .brand--cover .brand-tagline {
    font-size: 6px;
    letter-spacing: 2px;
    margin-top: 5px;
    opacity: 0.85;
  }
  .brand--inside {
    left: 0;
    width: 480px;
    top: 322px;
    color: var(--ink);
  }
  .brand--inside .brand-name { font-size: 31px; }
  .brand--inside .brand-rule {
    width: 300px;
    height: 1px;
    margin: 8px auto 7px;
    background: var(--rule);
  }
  .brand--inside .brand-tagline {
    font-size: 9px;
    letter-spacing: 3.2px;
  }
  .inside-rule {
    position: absolute;
    height: 1px;
    background: var(--rule);
  }
  .inside-rule--top { left: 70px; top: 41px; width: 276px; }
  .inside-rule--bottom { left: 82px; top: 634px; width: 386px; }
  .contact {
    position: absolute;
    left: 12px;
    top: 574px;
    padding-left: 12px;
    border-left: 3px solid var(--paper);
    color: var(--paper);
    font-family: "Montserrat", sans-serif;
    font-size: 11px;
    line-height: 15px;
  }
  .contact-web { font-weight: 600; }
</style>
</head>
<body>
<div class="canvas">
  <svg class="folder-flap" width="1200" height="1200" viewBox="0 0 1200 1200" aria-hidden="true">
    <path d="M176 478 L118 486 L118 500 L100 506 L100 530 L92 536 L92 900 Q92 930 130 936 L176 936 Z" fill="var(--navy-dark)"/>
    <path d="M176 936 L176 948 Q400 958 560 948 L600 936 Z" fill="var(--navy-dark)"/>
  </svg>

  <section class="folder-cover">
    <div class="brand brand--cover">
      <div class="brand-name">Moreira, Campos &amp; Lacerda</div>
      <div class="brand-tagline">Advocacia e Consultoria Jurídica</div>
    </div>
    <address class="contact" style="font-style:normal">
      End. exemplo dos exemplos I 000<br>
      Bairro I Cidade/SP<br>
      CEP 00000-00<br>
      Tel. 00 (00) 0000-0000<br>
      <span class="contact-web">www.siteexemplo.com.br</span>
    </address>
  </section>

  <section class="folder-inside">
    <div class="inside-rule inside-rule--top"></div>
    <div class="brand brand--inside">
      <div class="brand-name">Moreira, Campos &amp; Lacerda</div>
      <div class="brand-rule"></div>
      <div class="brand-tagline">Advocacia e Consultoria Jurídica</div>
    </div>
    <div class="inside-rule inside-rule--bottom"></div>
  </section>
</div>
</body>
</html>
```